Website design for Cambridge based systematic hedge fund

We have run previous pixelarena competitions to design our company logo, business cards and the styling of our presentation deck (see attached files).
As the final step we are looking to get a website designed that is thematically consistent with these existing elements of our branding.
You can find some of our competitors websites below:
https://www.quellmarsh.example/
https://www.fenvork.example/
https://www.lupitrel.example/
https://www.grastol.example/
https://www.movelhurst.example/
https://www.ostrivel.example/
https://www.yendrapeak.example/home
We would like to have a website that works well on both mobile devices and desktops. Either just as one page that can be scrolled down, with links at the top that skips to certain sections, or a few separate pages that can be navigated by a top menu.
It should look professional, we are not after lots of animations or unnecessary transitions, and in particular the website must be smooth to navigate. We would like to avoid having peoples of people, we are happy to make use of elements from the presentation (for example the style of the cover slide, or the section slides with the faded bridge in the background), or 'financial' style images.
We would like to have the following sections for now. For some of these some example text has been provided, final text may change but it will be of similar length. For the other sections we are happy to just have template text for now. At the moment we are mainly interested to see styles/layouts as words can be added easily afterwards:
1) We will need a disclaimer pop up the first time someone visits the site (see for example the yendrapeak example).
2) Top page - company name, then in larger text "Bringing AI and Statistical Inference to Financial Markets", and somewhere in smaller text "Pellworth Engines is a quantitative asset manager with the singular focus of delivering algorithmic strategies that work"
3) "About us" section: will describe us as a company, details our approach, company values, and explains the company logo.
Example text:
"We deliver consistent alpha across liquid markets through the application of proprietary IP in Bayesian inference, machine learning and artificial intelligence. We are a multi-disciplinary team founded by experienced finance professionals from premier institutions, leading academics from the Halvorsen Stellar Unit at Dunmoor College and world-class software engineers.
Our logo portrays a sillhoute of the mathematical bridge at Dunmoor College. Our unique scientific approach allows us to bridge cutting-edge mathematical research and computing expertise with financial knowledge to bring algorithmns that work to liquid markets"
4) Hiring section, detailing our culture, what we are looking for.
Example text:
"We are always looking for exceptional talent to join our entrepreneurial team. We are looking for individuals who are creative thinkers, can demonstrate analytical rigour and are passionate about the intersection of science, finance and technology.
We prioritise having a company culture that promotes sharing ideas in a safe, collaborative research environment. We make sure that every member of the team has the oppertunity to explore their own ideas through weekly 'innovation time', and ensure that everyone gets the support they need to continue to grow as individuals within the company."
5) A section for news/press releases
6) Contact us area at the bottom with office location and email. We will need to list 3 addresses for our Cambridge, London and Singapore offices, along with a couple of contact emails or phone numbers
7) A client login button at the top that will take them to a different website (unrelated to this one).

```html
<!DOCTYPE html>
<html lang="en">
<head>
<meta charset="utf-8">
<title>Pellworth Engines</title>
<link href="https://fonts.googleapis.com/css2?family=Montserrat:wght@400;500;600;700&display=swap" rel="stylesheet">
<style>
:root{
  --backdrop:#b7d3f5;
  --navy:#0a3f73;
  --navy-deep:#083563;
  --orange:#ff8500;
  --light:#f3f5f9;
  --white:#ffffff;
  --ink:#1c2533;
  --muted:#6b7686;
  --accent:#4a8fd6;
  --line:#e3e8ef;
}
*{box-sizing:border-box;margin:0;padding:0}
html,body{width:1200px;height:4874px;overflow:hidden}
body{background:var(--backdrop);font-family:'Montserrat',sans-serif;color:var(--ink);position:relative}
.page{position:absolute;left:300px;top:0;width:600px;height:4874px;background:var(--white);overflow:hidden}
.section{position:absolute;left:0;width:600px}
.abs{position:absolute}
.btn{position:absolute;background:var(--orange);color:var(--white);font-size:6px;font-weight:600;display:flex;align-items:center;justify-content:center;border-radius:2px}
.eyebrow{font-size:5px;color:var(--accent);font-weight:500}
.small{font-size:5px;line-height:1.6;color:var(--muted)}
.navy{background:var(--navy);color:var(--white)}
.rule{position:absolute;height:1px;width:30px;background:var(--accent)}

/* disclaimer */
.disclaimer{top:0;height:337px}
.modal{left:112px;top:38px;width:378px;height:261px;background:var(--white);text-align:center}
.modal h2{position:absolute;top:44px;width:100%;font-size:14px;font-weight:600;color:var(--ink);letter-spacing:.5px}
.modal p{position:absolute;top:78px;left:55px;width:268px;font-size:7px;line-height:1.65;color:#444}
.modal .close{position:absolute;right:14px;top:10px;font-size:11px;color:#999}

/* nav */
.nav{top:337px;height:32px;background:var(--white);border-bottom:1px solid var(--line)}
.brand{font-weight:700;color:var(--navy);font-size:6px}
.nav .brand{left:45px;top:12px}
.nav ul{position:absolute;left:284px;top:13px;display:flex;gap:12px;list-style:none;font-size:5px;font-weight:600;color:var(--navy)}

/* hero */
.hero{top:369px;height:307px}
.hero .net{right:0;top:0;width:332px;height:307px;background:radial-gradient(ellipse at 60% 50%,#1d6fc4 0%,#0f4f93 40%,var(--navy) 75%)}
.hero .eyebrow{left:45px;top:68px;font-size:6px;font-weight:700;color:var(--white)}
.hero h1{position:absolute;left:45px;top:84px;font-size:17px;line-height:1.55;font-weight:700;width:330px}
.hero p{position:absolute;left:45px;top:143px;width:200px;font-size:5.5px;line-height:1.6;color:#cfdbea}

/* about */
.about{top:676px;height:872px;background:var(--light)}
.about .card{left:64px;top:62px;width:239px;height:299px;background:var(--white)}
.about .card h3{position:absolute;left:18px;top:66px;font-size:14px;line-height:1.4;font-weight:700;width:200px}
.about .card .eyebrow{position:absolute;left:18px;top:51px}
.about .card p{position:absolute;left:18px;top:121px;width:185px}
.photo{position:absolute}
.about .wordmark{left:0;top:486px;width:600px;display:flex;align-items:center;justify-content:center;gap:10px;color:var(--navy);font-weight:700;font-size:24px}
.about .wordmark .mark{width:18px;height:18px;background:var(--navy)}
.about .mission{left:125px;top:563px;width:350px;text-align:center}
.partners-title{position:absolute;left:64px;top:652px;font-size:16px;font-weight:700;color:var(--navy)}
.partners{position:absolute;left:64px;top:725px;display:flex;gap:9px}
.partner{width:111px;height:70px;background:var(--white);border:1px solid var(--line);display:flex;align-items:center;justify-content:center}

/* approach */
.approach{top:1548px;height:303px;text-align:center}
.approach h2{position:absolute;top:26px;width:100%;font-size:16px;font-weight:700}
.approach .intro{position:absolute;left:190px;top:52px;width:220px;font-size:5px;line-height:1.7;color:#cfdbea}
.step{position:absolute;top:146px;width:95px;text-align:left}
.step .num{width:20px;height:20px;border-radius:50%;background:var(--accent);font-size:8px;display:flex;align-items:center;justify-content:center}
.step h4{margin-top:8px;font-size:6px;font-weight:600;line-height:1.6}
.step p{margin-top:7px;font-size:4.6px;line-height:1.7;color:#cfdbea}

/* story */
.story{top:1851px;height:1356px;background:var(--white)}
.story h2{position:absolute;font-weight:700;color:var(--ink)}
.feature{position:absolute;width:92px;padding:6px}
.feature.raised{background:var(--white);box-shadow:0 2px 8px rgba(10,63,115,.12)}
.feature svg{display:block}
.feature h5{font-size:5px;font-weight:600;margin:5px 0 4px}
.col-title{position:absolute;font-size:14px;font-weight:700;line-height:1.4;width:200px}

/* hiring */
.hiring{top:3207px;height:607px}
.hiring h2{position:absolute;top:42px;width:100%;text-align:center;font-size:16px;font-weight:700}
.hiring .para{position:absolute;top:106px;width:205px;font-size:5px;line-height:1.75;color:#cfdbea}
.filters{position:absolute;left:45px;top:204px;display:flex;gap:6px}
.chip{height:18px;border:1px solid #5c86b3;border-radius:9px;padding:0 14px;font-size:5px;display:flex;align-items:center}
.chip.on{background:var(--white);color:var(--navy)}
.showing{position:absolute;left:45px;top:256px;font-size:6px}
.job{position:absolute;width:250px;height:52px;background:var(--white);color:var(--navy);padding:12px 12px}
.job h5{font-size:7px;font-weight:600}
.job p{font-size:5.5px;color:var(--accent);margin-top:6px}
.show-more{position:absolute;top:490px;width:100%;text-align:center;font-size:6px;font-weight:600;text-decoration:underline}
.cta{position:absolute;left:45px;top:541px;font-size:7px;font-weight:600;line-height:1.65;width:280px}

/* news & contact */
.news{top:3814px;height:903px;background:var(--light)}
.news h2,.contact-title{position:absolute;width:100%;text-align:center;font-size:16px;font-weight:700}
.news h4{font-size:7px;font-weight:600;line-height:1.55}
.date{font-size:4.5px;color:var(--muted)}
.news-card{position:absolute;top:237px;width:149px}
.news-card .img{height:91px}
.news-card .eyebrow{margin-top:12px}
.news-card h4{margin:4px 0 8px}
.offices{position:absolute;left:64px;top:720px;width:474px;height:134px;background:var(--white);display:flex;padding:18px 22px;gap:20px;box-shadow:0 2px 10px rgba(10,63,115,.08)}
.office{flex:1}
.office h5{font-size:7px;color:var(--accent);font-weight:600;margin-bottom:12px}
.office .row{display:flex;gap:6px;align-items:flex-start;font-size:4.6px;color:var(--muted);line-height:1.6;margin-bottom:8px;padding-left:20px}
.office svg{flex:none}

/* footer */
.footer{top:4717px;height:157px;text-align:center}
.footer .brand{position:absolute;top:16px;width:100%;color:var(--white);font-size:8px}
.footer ul{position:absolute;top:57px;width:100%;display:flex;justify-content:center;gap:14px;list-style:none;font-size:5px;font-weight:600}
.social{position:absolute;top:76px;width:100%;display:flex;justify-content:center;gap:5px}
.social span{width:7px;height:7px;border-radius:50%;border:1px solid var(--white)}
.footer .divider{position:absolute;left:0;top:136px;width:600px;height:1px;background:#285a8d}
.footer .copy{position:absolute;top:145px;width:100%;font-size:4.5px;color:#cfdbea}
</style>
</head>
<body>
<div class="page">

  <section class="section disclaimer navy">
    <div class="abs modal">
      <span class="close">×</span>
      <h2>DISCLAIMER</h2>
      <p>Lorem ipsum dolor sit amet, consetetur sadipscing elitr, sed diam nonumy eirmod tempor invidunt ut labore et dolore magna aliquyam erat, sed diam voluptua. At vero eos et accusam et justo duo dolores et ea rebum. Stet clita kasd gubergren, no sea takimata sanctus est Lorem ipsum dolor sit amet. Lorem ipsum dolor sit amet, consetetur sadipscing elitr.</p>
      <div class="btn" style="left:147px;top:197px;width:84px;height:22px">I AGREE</div>
    </div>
  </section>

  <header class="section nav">
    <div class="abs brand">Pellworth Engines</div>
    <ul><li>HOME</li><li>ABOUT</li><li>APPROACH</li><li>VALUE</li><li>CULTURE</li></ul>
    <div class="btn" style="left:500px;top:8px;width:55px;height:16px">Login</div>
  </header>

  <section class="section hero navy">
    <div class="abs net" role="img" aria-label="Glowing blue network of connected data points"></div>
    <div class="abs eyebrow">PELLWORTH ENGINES</div>
    <h1>Bringing AI and Statistical Inference to Financial Markets</h1>
    <p>Pellworth Engines is a quantitative asset manager with the singular focus of delivering algorithmic strategies that work</p>
    <div class="btn" style="left:45px;top:195px;width:66px;height:20px">Contact us</div>
  </section>

  <section class="section about">
    <div class="abs card">
      <span class="eyebrow">About us</span>
      <h3>Lorem Ipsum is simply dummy text</h3>
      <p class="small">We deliver consistent alpha across liquid markets through the application of proprietary IP in Bayesian inference, machine learning and artificial intelligence. We are a multi-disciplinary team founded by experienced finance professionals from premier institutions, leading academics from the Halvorsen Stellar Unit at Dunmoor College and world-class software engineers.</p>
      <div class="btn" style="left:18px;top:231px;width:66px;height:18px">Read more</div>
    </div>
    <div class="photo" role="img" aria-label="Team reviewing printed charts on a desk with a laptop, viewed from above" style="left:303px;top:62px;width:235px;height:299px;background:linear-gradient(135deg,#8a94a3,#d9dde3 55%,#5d6673)"></div>
    <div class="abs wordmark"><span class="mark"></span><span>Pellworth Engines</span></div>
    <p class="abs small mission">Our logo portrays a silhouette of the mathematical bridge at Dunmoor College. Our unique scientific approach allows us to bridge cutting-edge mathematical research and computing expertise with financial knowledge to bring algorithms that work to liquid markets.</p>
    <h3 class="partners-title">Our Partners</h3>
    <div class="rule" style="left:64px;top:686px"></div>
    <div class="partners">
      <div class="partner"><svg width="40" height="16"><rect x="0" y="3" width="40" height="10" rx="5" fill="#d5dbe3"/></svg></div>
      <div class="partner"><svg width="40" height="16"><rect x="0" y="3" width="40" height="10" rx="2" fill="#d5dbe3"/></svg></div>
      <div class="partner"><svg width="40" height="16"><circle cx="8" cy="8" r="7" fill="#d5dbe3"/></svg></div>
      <div class="partner"><svg width="40" height="16"><rect x="12" y="1" width="16" height="14" fill="#d5dbe3"/></svg></div>
    </div>
  </section>

  <section class="section approach navy">
    <h2>Approach</h2>
    <p class="intro">Lorem Ipsum is simply dummy text of the printing and typesetting industry. Lorem Ipsum has been the industry standard dummy text ever since the 1500s.</p>
    <div class="rule" style="left:285px;top:96px"></div>
    <div class="step" style="left:64px"><div class="num">01</div><h4>Lorem Ipsum is simply dummy</h4><p>Lorem Ipsum is simply dummy text of the printing and typesetting industry.</p></div>
    <div class="step" style="left:192px"><div class="num">02</div><h4>Lorem Ipsum is simply dummy</h4><p>Lorem Ipsum is simply dummy text of the printing and typesetting industry.</p></div>
    <div class="step" style="left:321px"><div class="num">03</div><h4>Lorem Ipsum is simply dummy</h4><p>Lorem Ipsum is simply dummy text of the printing and typesetting industry.</p></div>
    <div class="step" style="left:449px"><div class="num">04</div><h4>Lorem Ipsum is simply dummy</h4><p>Lorem Ipsum is simply dummy text of the printing and typesetting industry.</p></div>
  </section>

  <section class="section story">
    <span class="abs eyebrow" style="left:64px;top:66px">Our company values</span>
    <h2 style="left:64px;top:80px;font-size:14px;line-height:1.45">Know more<br>About</h2>
    <p class="abs small" style="left:64px;top:143px;width:220px">Lorem Ipsum is simply dummy text of the printing and typesetting industry. Lorem Ipsum has been the industry's standard dummy text ever since the 1500s.</p>
    <div class="feature raised" style="left:50px;top:200px">
      <svg width="10" height="8"><path d="M1 4l3 3 5-6" stroke="#4a8fd6" fill="none" stroke-width="1.4"/></svg>
      <h5>Lorem Ipsum is</h5><p class="small" style="font-size:4.2px">Lorem Ipsum is simply dummy text of the printing and typesetting.</p>
    </div>
    <div class="feature" style="left:170px;top:200px">
      <svg width="10" height="8"><path d="M1 4l3 3 5-6" stroke="#4a8fd6" fill="none" stroke-width="1.4"/></svg>
      <h5>Lorem Ipsum is</h5><p class="small" style="font-size:4.2px">Lorem Ipsum is simply dummy text of the printing and typesetting.</p>
    </div>
    <div class="feature" style="left:50px;top:298px">
      <svg width="10" height="8"><path d="M1 4l3 3 5-6" stroke="#4a8fd6" fill="none" stroke-width="1.4"/></svg>
      <h5>Lorem Ipsum is</h5><p class="small" style="font-size:4.2px">Lorem Ipsum is simply dummy text of the printing and typesetting.</p>
    </div>
    <div class="feature" style="left:170px;top:298px">
      <svg width="10" height="8"><path d="M1 4l3 3 5-6" stroke="#4a8fd6" fill="none" stroke-width="1.4"/></svg>
      <h5>Lorem Ipsum is</h5><p class="small" style="font-size:4.2px">Lorem Ipsum is simply dummy text of the printing and typesetting.</p>
    </div>
    <div class="photo" role="img" aria-label="Hand holding a printed stock chart report" style="left:310px;top:70px;width:228px;height:299px;background:linear-gradient(160deg,#1f3552,#4d6a8c 50%,#c9d2dc)"></div>

    <span class="abs eyebrow" style="left:64px;top:467px">Our company values</span>
    <h2 style="left:64px;top:478px;font-size:24px;line-height:1.35">Lorem Ipsum is simply<br>dummy text</h2>
    <p class="abs small" style="left:64px;top:566px;width:474px">Lorem ipsum dolor sit amet, consetetur sadipscing elitr, sed diam nonumy eirmod tempor invidunt ut labore et dolore magna aliquyam erat, sed diam voluptua. At vero eos et accusam et justo duo dolores et ea rebum. Stet clita kasd gubergren, no sea takimata sanctus est Lorem ipsum dolor sit amet. Lorem ipsum dolor sit amet, consetetur sadipscing elitr, sed diam nonumy eirmod tempor invidunt ut labore et dolore magna aliquyam erat.</p>
    <div class="photo" role="img" aria-label="Printed financial reports with bar and line charts spread across a desk" style="left:45px;top:629px;width:555px;height:250px;background:linear-gradient(120deg,#e9ecef,#f7f8fa 45%,#cfd6de)"></div>

    <h3 class="col-title" style="left:45px;top:951px">Lorem Ipsum is simply dummy text</h3>
    <p class="abs small" style="left:45px;top:995px;width:180px">Lorem ipsum dolor sit amet, consetetur sadipscing elitr, sed diam nonumy eirmod tempor invidunt ut labore et dolore magna aliquyam.</p>
    <div class="photo" role="img" aria-label="Hands holding an infographic printout with pie and bar charts" style="left:45px;top:1051px;width:218px;height:250px;background:linear-gradient(150deg,#e3d7c7,#f5f1eb 50%,#b8a48c)"></div>
    <h3 class="col-title" style="left:337px;top:951px">Lorem Ipsum is simply dummy text</h3>
    <p class="abs small" style="left:337px;top:995px;width:180px">Lorem ipsum dolor sit amet, consetetur sadipscing elitr, sed diam nonumy eirmod tempor invidunt ut labore et dolore magna aliquyam.</p>
    <div class="photo" role="img" aria-label="Laptop beside printed colourful bar chart reports" style="left:337px;top:1051px;width:218px;height:250px;background:linear-gradient(200deg,#d6c9b6,#eef0f3 50%,#9fb4cc)"></div>
  </section>

  <section class="section hiring navy">
    <h2>We are Hiring</h2>
    <div class="rule" style="left:285px;top:72px"></div>
    <p class="para" style="left:45px">We are always looking for exceptional talent to join our entrepreneurial team. We are looking for individuals who are creative thinkers, can demonstrate analytical rigour and are passionate about the intersection of science, finance and technology.</p>
    <p class="para" style="left:335px;width:220px">We prioritise having a company culture that promotes sharing ideas in a safe, collaborative research environment. We make sure that every member of the team has the opportunity to explore their own ideas through weekly 'innovation time', and ensure that everyone gets the support they need to continue to grow as individuals within the company.</p>
    <div class="filters"><span class="chip on">All Jobs</span><span class="chip">Business</span><span class="chip">Growth and Marketing</span></div>
    <p class="showing">Showing all jobs (20)</p>
    <div class="job" style="left:45px;top:278px"><h5>Lorem Ipsum is simply dummy text</h5><p>Lorem Ipsum is simply</p></div>
    <div class="job" style="left:305px;top:278px"><h5>Lorem Ipsum is simply dummy text</h5><p>Lorem Ipsum is simply</p></div>
    <div class="job" style="left:45px;top:344px"><h5>Lorem Ipsum is simply dummy text</h5><p>Lorem Ipsum is simply</p></div>
    <div class="job" style="left:305px;top:344px"><h5>Lorem Ipsum is simply dummy text</h5><p>Lorem Ipsum is simply</p></div>
    <div class="job" style="left:45px;top:409px"><h5>Lorem Ipsum is simply dummy text</h5><p>Lorem Ipsum is simply</p></div>
    <div class="job" style="left:305px;top:409px"><h5>Lorem Ipsum is simply dummy text</h5><p>Lorem Ipsum is simply</p></div>
    <p class="show-more">Show more</p>
    <p class="cta">Can't find your fit? Drop your CV and we'll reach out when an opportunity comes up!</p>
    <div class="btn" style="left:457px;top:538px;width:98px;height:28px;font-size:7px">Drop your CV</div>
  </section>

  <section class="section news">
    <h2 style="top:38px">News releases</h2>
    <div class="photo" role="img" aria-label="Desk with laptops and printed reports viewed from above" style="left:64px;top:86px;width:236px;height:132px;background:linear-gradient(135deg,#6f5a4a,#c9c2b8 50%,#3f4a58)"></div>
    <div class="abs" style="left:316px;top:95px;width:174px">
      <span class="eyebrow">Press release</span>
      <h4 style="margin:5px 0 7px">Lorem Ipsum is simply dummy text of the printing</h4>
      <p class="small" style="font-size:4.4px">Lorem ipsum dolor sit amet, consetetur sadipscing elitr, sed diam nonumy eirmod tempor invidunt ut labore et dolore magna aliquyam erat.</p>
      <p class="date" style="margin-top:8px">12.05.2021</p>
    </div>
    <div class="news-card" style="left:64px"><div class="img" role="img" aria-label="Laptop showing financial charts" style="background:linear-gradient(135deg,#a99a88,#e6e2dc)"></div><div class="eyebrow">Press release</div><h4>Lorem ipsum dolor sit amet, consetetur sadipscing elitr, sed diam nonum</h4><p class="date">03.04.2021</p></div>
    <div class="news-card" style="left:226px"><div class="img" role="img" aria-label="Hand pointing at printed graphs" style="background:linear-gradient(135deg,#2c4a6e,#c6d2df)"></div><div class="eyebrow">Press release</div><h4>Lorem ipsum dolor sit amet, consetetur sadipscing elitr, sed diam nonum</h4><p class="date">21.03.2021</p></div>
    <div class="news-card" style="left:389px"><div class="img" role="img" aria-label="Analyst working with charts on a desk" style="background:linear-gradient(135deg,#3b4856,#d8dde3)"></div><div class="eyebrow">Press release</div><h4>Lorem ipsum dolor sit amet, consetetur sadipscing elitr, sed diam nonum</h4><p class="date">09.02.2021</p></div>

    <h2 class="contact-title" style="top:488px">Contact us</h2>
    <div class="photo" role="img" aria-label="Street map showing the office location" style="left:45px;top:549px;width:510px;height:199px;background:linear-gradient(180deg,#dfe6d8,#e8ecee 60%,#d3dee8)"></div>
    <div class="offices">
      <div class="office">
        <h5>Cambridge</h5>
        <div class="row"><svg width="6" height="6"><path d="M1 1h1.5l.8 1.6-.9.6a4 4 0 002 2l.6-.9 1.6.8V6.6C3 6.6 0 3.6 0 .6" fill="#8793a2"/></svg><span>+44 1223 000 100</span></div>
        <div class="row"><svg width="6" height="5"><rect x=".3" y=".3" width="5.4" height="4.4" fill="none" stroke="#8793a2" stroke-width=".6"/><path d="M.3.3L3 2.6 5.7.3" fill="none" stroke="#8793a2" stroke-width=".6"/></svg><span>hello@pellworth.example</span></div>
        <div class="row"><svg width="5" height="7"><path d="M2.5 7S0 4 0 2.5a2.5 2.5 0 015 0C5 4 2.5 7 2.5 7z" fill="#8793a2"/></svg><span>4 Mill Road, Cambridge CB1 2AB, sed diam nonumy eirmod tempor.</span></div>
      </div>
      <div class="office">
        <h5>London</h5>
        <div class="row"><svg width="6" height="6"><path d="M1 1h1.5l.8 1.6-.9.6a4 4 0 002 2l.6-.9 1.6.8V6.6C3 6.6 0 3.6 0 .6" fill="#8793a2"/></svg><span>+44 20 0000 0200</span></div>
        <div class="row"><svg width="6" height="5"><rect x=".3" y=".3" width="5.4" height="4.4" fill="none" stroke="#8793a2" stroke-width=".6"/><path d="M.3.3L3 2.6 5.7.3" fill="none" stroke="#8793a2" stroke-width=".6"/></svg><span>london@pellworth.example</span></div>
        <div class="row"><svg width="5" height="7"><path d="M2.5 7S0 4 0 2.5a2.5 2.5 0 015 0C5 4 2.5 7 2.5 7z" fill="#8793a2"/></svg><span>18 Ferrow Lane, London EC2 4XY, sed diam nonumy eirmod tempor.</span></div>
      </div>
      <div class="office">
        <h5>Singapore</h5>
        <div class="row"><svg width="6" height="6"><path d="M1 1h1.5l.8 1.6-.9.6a4 4 0 002 2l.6-.9 1.6.8V6.6C3 6.6 0 3.6 0 .6" fill="#8793a2"/></svg><span>+65 6000 0300</span></div>
        <div class="row"><svg width="6" height="5"><rect x=".3" y=".3" width="5.4" height="4.4" fill="none" stroke="#8793a2" stroke-width=".6"/><path d="M.3.3L3 2.6 5.7.3" fill="none" stroke="#8793a2" stroke-width=".6"/></svg><span>asia@pellworth.example</span></div>
        <div class="row"><svg width="5" height="7"><path d="M2.5 7S0 4 0 2.5a2.5 2.5 0 015 0C5 4 2.5 7 2.5 7z" fill="#8793a2"/></svg><span>9 Tessan Quay, Singapore 049000, sed diam nonumy eirmod tempor.</span></div>
      </div>
    </div>
  </section>

  <footer class="section footer navy">
    <div class="brand">Pellworth Engines</div>
    <ul><li>HOME</li><li>ABOUT</li><li>APPROACH</li><li>VALUE</li><li>CULTURE</li></ul>
    <div class="social"><span></span><span></span><span></span><span></span><span></span></div>
    <div class="divider"></div>
    <p class="copy">© 2021 Pellworth Engines - All Rights Reserved</p>
  </footer>

</div>
</body>
</html>
```